Summit Builders Web Site / Business Cards

Construction Company that specializes in Water and Fire Damage, Residential ReModels, Landscaping and Building ADU (Accessory Dwelling Unit)

Growing and changing families often need additional space, and a remodeling project can often provide that. Adding a new area, or repurposing an existing one can satisfy this requirement.

Other times, homeowners want to update the look in their kitchen or bathroom with more than just a change of cabinetry or vanity doors and drawers. Whatever your needs are, Summit Builders has skilled workers who are bonded and insured, and ready to make your dreams and visions a reality.

Target Market(s)

Home Owners

Industry/Entity Type

Construction Company

Contact Information for Business Card

Center Logo with our information on the corners

Back side to be Logo Only
Contact Info
CSLB License # 4829516
info@summitbuildersca.example
www.summitbuildersca.example

Coding

Coded - Design and coding required

Number of Pages Required

5+ page

Font styles to use
Serif
Sans Serif

Requirements
Must have
• Using our Logo Colors
Home
About Us
Services
Projects / Portfolio
Contact Us
Nice to have
• Colors matching our Logo
Should not have
• Black because it doesnt match our logo

```html
<!DOCTYPE html>
<html lang="en">
<head>
<meta charset="utf-8">
<title>Summit Builders</title>
<link href="https://fonts.googleapis.com/css2?family=Mulish:wght@400;600;700;800&family=Raleway:wght@700;800;900&display=swap" rel="stylesheet">
<style>
:root{
  --orange:#f26b0a;
  --orange-deep:#c4520a;
  --ink:#3a2a20;
  --muted:#6e6058;
  --line:#e8e2dc;
  --brown-1:#5a3c28;
  --brown-2:#7a5238;
  --brown-3:#9a5a26;
  --footer-1:#4a3324;
  --footer-2:#6a4226;
  --footer-text:#e0cfc2;
  --white:#ffffff;
}
*{box-sizing:border-box;margin:0;padding:0}
html,body{width:1200px;height:4264px;overflow:hidden}
body{position:relative;font-family:'Mulish',sans-serif;color:var(--ink);background:var(--white)}
.abs{position:absolute}
.head{font-family:'Raleway',sans-serif;font-weight:800;color:var(--ink)}
.btn{position:absolute;display:flex;align-items:center;justify-content:center;gap:8px;background:var(--orange);color:var(--white);font-weight:700;font-size:12px;border-radius:2px;box-shadow:3px 3px 0 var(--orange-deep)}
.btn-ghost{position:absolute;display:flex;align-items:center;justify-content:center;border:1px solid #bbb;color:var(--ink);font-size:11px;font-weight:700;border-radius:2px;background:var(--white)}

/* top bar */
.topbar{top:0;left:0;width:1200px;height:45px;background:#f4f2f0}
.topbar .item{position:absolute;top:14px;font-size:12px;color:#4a3a30;display:flex;align-items:center;gap:8px;white-space:nowrap}
.topbar .sep{position:absolute;top:0;width:1px;height:45px;background:#ddd}
.nav{top:45px;left:0;width:1200px;height:55px;background:var(--white)}
.brand{position:absolute;display:flex;align-items:center;gap:8px;font-family:'Raleway',sans-serif;font-weight:800;color:var(--ink)}
.brand .mark{width:22px;height:22px;background:var(--orange)}
.nav .link{position:absolute;top:20px;font-size:11.5px;color:#4a3a30}
.nav .active{color:var(--orange);font-weight:700}
.nav .active::before{content:"";position:absolute;left:-2px;right:-2px;top:-20px;height:2px;background:var(--orange)}

/* hero */
.hero{top:100px;left:0;width:1200px;height:503px;background:radial-gradient(ellipse at 60% 30%,#a07a58 0%,var(--brown-2) 40%,var(--brown-1) 100%)}
.hero .kicker{position:absolute;top:146px;width:100%;text-align:center;color:var(--white);font-size:20px}
.hero h1{position:absolute;top:172px;width:100%;text-align:center;color:var(--white);font-family:'Raleway',sans-serif;font-weight:900;font-size:66px;letter-spacing:1px}
.hero .sub{position:absolute;top:250px;width:100%;text-align:center;color:var(--white);font-size:16px;font-weight:600}
.social{position:absolute;right:0;width:36px;height:36px}

/* clients */
.section-title{font-family:'Raleway',sans-serif;font-weight:800;font-size:23px;color:var(--ink)}
.section-title span{color:var(--orange)}
.client{position:absolute;top:741px;width:137px;height:83px;background:var(--white);box-shadow:0 2px 10px rgba(90,60,40,.12);display:flex;align-items:center;justify-content:center;gap:6px;font-weight:700;font-size:16px;color:#8a7d74}
.client i{display:block;width:10px;height:10px;border-radius:50%;background:#bbb}

.center-title{position:absolute;width:100%;text-align:center}
.rule{position:absolute;left:574px;width:52px;height:2px;background:#bbb}

/* cards */
.card{position:absolute;top:1084px;width:300px;height:462px;background:var(--white);box-shadow:0 6px 22px rgba(90,60,40,.12)}
.card .photo{width:300px;height:218px}
.card h3{position:absolute;top:258px;width:100%;text-align:center;font-weight:700;font-size:21px;color:var(--ink)}
.card .bar{position:absolute;top:304px;left:125px;width:50px;height:2px;background:#ccc}
.card p{position:absolute;top:326px;left:45px;width:210px;text-align:center;font-size:11px;line-height:18px;color:var(--muted)}
.card .btn-ghost,.card .btn{top:397px;left:96px;width:109px;height:32px}

/* stats */
.stats{top:1667px;left:0;width:1200px;height:294px;background:linear-gradient(180deg,#f07a22 0%,#f26b0a 60%,#e85f05 100%)}
.stat{position:absolute;top:80px;width:220px;text-align:center;color:var(--white)}
.stat .num{font-family:'Raleway',sans-serif;font-weight:800;font-size:40px;margin-top:8px;line-height:48px}
.stat .lbl{font-size:12px;font-weight:600}

/* who */
.feat{position:absolute;font-family:'Raleway',sans-serif;font-weight:800;font-size:12.5px;line-height:17px;color:var(--ink)}
.ring{position:absolute;width:58px;height:58px;border-radius:50%;background:var(--white);box-shadow:0 3px 12px rgba(90,60,40,.18);display:flex;align-items:center;justify-content:center}

/* projects */
.projects{top:2598px;left:0;width:1200px;height:543px;background:linear-gradient(100deg,var(--brown-1) 0%,var(--brown-2) 50%,var(--brown-3) 100%)}
.tile{position:absolute;border:3px solid var(--white)}
.play{position:absolute;width:70px;height:70px;border-radius:50%;background:var(--white);display:flex;align-items:center;justify-content:center}

/* testimonial */
.panel{position:absolute;top:3447px;left:0;width:576px;height:227px;background:var(--white);box-shadow:0 6px 22px rgba(90,60,40,.12)}

/* footer */
.footer{top:3762px;left:0;width:1200px;height:455px;background:linear-gradient(110deg,var(--footer-1) 0%,var(--footer-1) 55%,var(--footer-2) 100%)}
.footer h4{position:absolute;top:76px;font-family:'Raleway',sans-serif;font-weight:800;font-size:17px;color:var(--white);white-space:nowrap}
.footer .uline{position:absolute;top:114px;width:36px;height:2px;background:#a08878}
.footer .txt{position:absolute;font-size:11px;color:var(--footer-text);line-height:17px}
.footer .lbl{font-weight:700;color:var(--white);font-size:13px}
.field{position:absolute;left:839px;width:310px;border-bottom:1px solid #8a6e5c;height:30px;font-size:11px;color:var(--footer-text);display:flex;align-items:center;gap:12px;padding-left:6px}
.copy{top:4217px;left:0;width:1200px;height:47px;background:var(--orange);color:var(--white);font-size:12px;font-weight:600;display:flex;align-items:center;justify-content:center}
</style>
</head>
<body>

<!-- top bar -->
<div class="abs topbar">
  <div class="sep" style="left:486px"></div>
  <div class="item" style="left:504px">ISO 9001:2017</div>
  <div class="sep" style="left:608px"></div>
  <div class="item" style="left:624px">
    <svg width="18" height="12" viewBox="0 0 18 12"><rect x="1" y="1" width="16" height="10" fill="none" stroke="#f26b0a" stroke-width="1.4"/><path d="M1 1l8 6 8-6" fill="none" stroke="#f26b0a" stroke-width="1.4"/></svg>
    office@summitbuildersca.example</div>
  <div class="sep" style="left:884px"></div>
  <div class="item" style="left:900px">
    <svg width="16" height="16" viewBox="0 0 16 16"><path d="M3 1l3 3-2 2c1 2 3 4 5 5l2-2 3 3-2 3C7 15 1 9 1 3z" fill="none" stroke="#f26b0a" stroke-width="1.5"/></svg>
    Call Us +1 555 014 2290</div>
</div>

<!-- nav -->
<div class="abs nav">
  <div class="brand" style="left:119px;top:-34px;height:90px;font-size:22px"><span class="mark"></span>Summit Builders</div>
  <div class="link active" style="left:384px">Home</div>
  <div class="link" style="left:455px">About Us</div>
  <div class="link" style="left:564px">Services</div>
  <div class="link" style="left:648px">Projects / Portfolio</div>
  <div class="link" style="left:786px">Contact Us</div>
  <div class="btn" style="left:903px;top:8px;width:183px;height:37px">
    <svg width="16" height="14" viewBox="0 0 16 14"><rect x="1" y="2" width="11" height="11" fill="none" stroke="#fff" stroke-width="1.4"/><path d="M6 9l8-8" stroke="#fff" stroke-width="1.6"/></svg>
    Get a Free Quote</div>
</div>

<!-- hero -->
<section class="abs hero" role="img" aria-label="Silhouettes of construction workers and an excavator against the evening sky">
  <div class="kicker">The Best Choose Us</div>
  <h1>BECAUSE WE DELIVER</h1>
  <div class="sub">We specializes in Water and Fire Damage, Residential ReModels, Landscaping and Building ADU</div>
  <div class="btn" style="left:508px;top:300px;width:184px;height:41px">
    <svg width="16" height="14" viewBox="0 0 16 14"><rect x="1" y="2" width="11" height="11" fill="none" stroke="#fff" stroke-width="1.4"/><path d="M6 9l8-8" stroke="#fff" stroke-width="1.6"/></svg>
    Get a Free Quote</div>
  <div class="social" style="top:408px;background:#3b5998" role="img" aria-label="Social link"></div>
  <div class="social" style="top:444px;background:#35a9e0" role="img" aria-label="Social link"></div>
  <div class="social" style="top:480px;background:#d6336c" role="img" aria-label="Social link"></div>
</section>

<!-- clients -->
<div class="abs section-title" style="left:114px;top:682px">OUR <span>CLIENTS</span></div>
<svg class="abs" style="left:1048px;top:688px" width="40" height="20" viewBox="0 0 40 20"><rect x="0.5" y="0.5" width="19" height="19" fill="none" stroke="#ccc"/><rect x="20.5" y="0.5" width="19" height="19" fill="none" stroke="#ccc"/><path d="M13 10H6m3-3l-3 3 3 3" fill="none" stroke="#999" stroke-width="1.4"/><path d="M26 10h7m-3-3l3 3-3 3" fill="none" stroke="#f26b0a" stroke-width="1.4"/></svg>
<div class="client" style="left:113px"><i></i>Northvale</div>
<div class="client" style="left:280px">Brightway</div>
<div class="client" style="left:447px"><i></i>Oakline</div>
<div class="client" style="left:616px">Ridgeway</div>
<div class="client" style="left:783px"><i></i>Stonefield</div>
<div class="client" style="left:950px">Larkspur</div>
<div class="abs" style="left:113px;top:887px;width:974px;height:1px;background:var(--line)"></div>

<!-- what we do -->
<div class="center-title head" style="top:968px;font-size:31px">WHAT WE DO</div>
<div class="center-title" style="top:1013px;font-size:13px;color:#4a3a30">We specializes in Water and Fire Damage, Residential ReModels, Landscaping and Building ADU (Accessory Dwelling Unit)</div>
<div class="rule" style="top:1054px"></div>

<svg class="abs" style="left:56px;top:1303px" width="22" height="24" viewBox="0 0 22 24"><path d="M8 2h12v20H8" fill="none" stroke="#5a4a40" stroke-width="1.5"/><path d="M14 12H2m4-4l-4 4 4 4" fill="none" stroke="#5a4a40" stroke-width="1.5"/></svg>
<svg class="abs" style="left:1122px;top:1303px" width="22" height="24" viewBox="0 0 22 24"><path d="M14 2H2v20h12" fill="none" stroke="#f26b0a" stroke-width="1.5"/><path d="M8 12h12m-4-4l4 4-4 4" fill="none" stroke="#f26b0a" stroke-width="1.5"/></svg>

<div class="card" style="left:113px">
  <div class="photo" role="img" aria-label="Builders reviewing plans outside a house under construction" style="background:linear-gradient(160deg,#cfd6dc,#8f8574 60%,#c9a23c)"></div>
  <h3>Home Construction</h3><div class="bar"></div>
  <p>Lorem Ipsum is simply dummy the printing and typesetting industry. Lorem Ipsum has been the industry.</p>
  <div class="btn-ghost">Read More</div>
</div>
<div class="card" style="left:450px">
  <div class="photo" role="img" aria-label="Blue two-storey house exterior at dusk" style="background:linear-gradient(180deg,#6f8fb8,#3d4c6a 55%,#4f7a3a)"></div>
  <h3>Exterior Design</h3><div class="bar"></div>
  <p>Lorem Ipsum is simply dummy the printing and typesetting industry. Lorem Ipsum has been the industry.</p>
  <div class="btn" style="box-shadow:none">Read More</div>
</div>
<div class="card" style="left:788px">
  <div class="photo" role="img" aria-label="Bright open-plan living room interior" style="background:linear-gradient(170deg,#eeeeee,#c4bcb4 55%,#7a6e66)"></div>
  <h3>Interior Design</h3><div class="bar"></div>
  <p>Lorem Ipsum is simply dummy the printing and typesetting industry. Lorem Ipsum has been the industry.</p>
  <div class="btn-ghost">Read More</div>
</div>

<!-- stats -->
<section class="abs stats" role="img" aria-label="Orange toned photo of workers on a construction site">
  <div class="stat" style="left:123px">
    <svg width="56" height="56" viewBox="0 0 56 56" fill="none" stroke="#fff" stroke-width="2"><circle cx="20" cy="14" r="7"/><path d="M8 50V32q12-8 24 0v18"/><rect x="32" y="26" width="18" height="24"/><path d="M36 34h10M36 40h10M36 46h6"/></svg>
    <div class="num">53</div><div class="lbl">TOTAL PROJECTS</div></div>
  <div class="stat" style="left:357px">
    <svg width="56" height="56" viewBox="0 0 56 56" fill="none" stroke="#fff" stroke-width="2"><path d="M18 16a10 10 0 0120 0z"/><circle cx="28" cy="22" r="8"/><path d="M12 52V40q16-10 32 0v12M28 34v18"/></svg>
    <div class="num">371</div><div class="lbl">STAFF MEMBERS</div></div>
  <div class="stat" style="left:598px">
    <svg width="56" height="56" viewBox="0 0 56 56" fill="none" stroke="#fff" stroke-width="2"><path d="M24 30s-9-10-9-16a9 9 0 0118 0c0 6-9 16-9 16z"/><circle cx="24" cy="14" r="3"/><path d="M6 34l12 4 14-4 18 6-6 12-14-4-12 4z"/></svg>
    <div class="num">15</div><div class="lbl">WORKING IN STATES</div></div>
  <div class="stat" style="left:853px">
    <svg width="56" height="56" viewBox="0 0 56 56" fill="none" stroke="#fff" stroke-width="2"><circle cx="24" cy="24" r="18"/><path d="M24 12v12l8 6"/><circle cx="42" cy="42" r="9"/><path d="M42 38v5h4"/></svg>
    <div class="num">2,600</div><div class="lbl">HOURS FOR WORK</div></div>
</section>

<!-- who we are -->
<div class="center-title head" style="top:2038px;font-size:31px">WHO WE ARE</div>
<div class="center-title" style="top:2081px;font-size:13px;color:#4a3a30">We Deliver Landmark Projects</div>
<div class="center-title" style="top:2143px;left:200px;width:800px;font-size:11.5px;line-height:19px;color:#4a3a30">We are rethoric question ran over her cheek When she reached the first hills of the Italic Mountains, she had a last view back on the skyline of her hometown Bookmarksgrove, the headline of Alphabet Village and the subline of her own road, the Line Lane.</div>

<svg class="abs" style="left:0;top:2200px" width="1200" height="260" viewBox="0 0 1200 260" fill="none">
  <path d="M509 56H558l40 46" stroke="#9a8a80" stroke-dasharray="4 4"/>
  <path d="M691 56H642l-40 46" stroke="#9a8a80" stroke-dasharray="4 4"/>
  <path d="M469 167H520l20-44" stroke="#9a8a80" stroke-dasharray="4 4"/>
  <path d="M731 167H680l-20-44" stroke="#9a8a80" stroke-dasharray="4 4"/>
  <rect x="540" y="102" width="120" height="132" fill="#f26b0a"/>
  <line x1="190" y1="236" x2="1010" y2="236" stroke="#7a6a60" stroke-width="3"/>
</svg>
<div class="ring" style="left:451px;top:2227px"><svg width="26" height="30" viewBox="0 0 26 30" fill="none" stroke="#f26b0a" stroke-width="2"><circle cx="13" cy="11" r="9"/><path d="M8 19l-3 9 8-4 8 4-3-9"/></svg></div>
<div class="ring" style="left:691px;top:2227px"><svg width="22" height="28" viewBox="0 0 22 28" fill="none" stroke="#f26b0a" stroke-width="2"><rect x="2" y="2" width="18" height="24"/><path d="M6 9h10M6 14h10M6 19h6"/></svg></div>
<div class="ring" style="left:411px;top:2338px"><svg width="30" height="22" viewBox="0 0 30 22" fill="none" stroke="#f26b0a" stroke-width="2"><path d="M2 6l8-4 6 4 6-4 6 4v8l-10 6-8-6-8 0z"/></svg></div>
<div class="ring" style="left:731px;top:2338px"><svg width="30" height="24" viewBox="0 0 30 24" fill="none" stroke="#f26b0a" stroke-width="2"><circle cx="9" cy="8" r="4"/><circle cx="21" cy="8" r="4"/><path d="M2 22q7-10 14 0M14 22q7-10 14 0"/></svg></div>
<div class="feat" style="left:280px;top:2244px;width:140px;text-align:right">WE'VE REPUTION<br>FOR EXCELLENCE</div>
<div class="feat" style="left:781px;top:2244px">GUIDED BY<br>COMMITMENT</div>
<div class="feat" style="left:241px;top:2349px;width:140px;text-align:right">WE BUILD<br>PARTNERSHIPS</div>
<div class="feat" style="left:819px;top:2349px">A TEAM OF<br>PROFESSIONALS</div>
<div class="center-title" style="top:2458px;font-family:'Raleway',sans-serif;font-weight:800;font-size:40px;color:var(--ink);letter-spacing:2px">Summit Builders</div>

<!-- recent projects -->
<section class="abs projects" role="img" aria-label="Warm toned background photo of a building under construction">
  <div class="abs head" style="left:114px;top:118px;font-size:33px;line-height:34px;color:var(--white)">RECENT<br>PROJECTS</div>
  <div class="abs" style="left:116px;top:198px;width:50px;height:2px;background:var(--orange)"></div>
  <div class="btn" style="left:116px;top:209px;width:109px;height:31px">View All</div>
  <div class="tile" role="img" aria-label="Suburban house lit at twilight" style="left:359px;top:90px;width:235px;height:178px;background:linear-gradient(180deg,#c9a07a,#7a8393 60%,#9a9fa6)"></div>
  <div class="tile" role="img" aria-label="School building with lettering on its facade" style="left:113px;top:278px;width:235px;height:179px;background:linear-gradient(160deg,#c8bfae,#9aa6b3 60%,#7f8a94)"></div>
  <div class="tile" role="img" aria-label="Two-storey brick family home" style="left:359px;top:278px;width:235px;height:179px;background:linear-gradient(180deg,#9bb4cf,#9a6a5a 55%,#5e7b4a)"></div>
  <div class="tile" role="img" aria-label="Engineers in hard hats looking at a building frame" style="left:606px;top:90px;width:480px;height:367px;background:linear-gradient(140deg,#6a5444,#8a6a4a 55%,#d9782a)">
    <div class="play" style="left:202px;top:146px"><svg width="22" height="26" viewBox="0 0 22 26"><path d="M3 2l17 11L3 24z" fill="none" stroke="#f26b0a" stroke-width="2"/></svg></div>
  </div>
</section>

<!-- testimonial -->
<div class="panel"></div>
<div class="abs" role="img" aria-label="Portrait video of a client speaking" style="left:114px;top:3240px;width:392px;height:370px;background:linear-gradient(180deg,#a89a90,#7a6c62)">
  <div class="play" style="left:161px;top:150px"><svg width="22" height="26" viewBox="0 0 22 26"><path d="M3 2l17 11L3 24z" fill="none" stroke="#f26b0a" stroke-width="2"/></svg></div>
</div>
<div class="abs head" style="left:645px;top:3262px;font-size:32px;line-height:41px">WHAT PEOPLE ARE<br>SAYING ABOUT SUMMIT<br>BUILDERS</div>
<svg class="abs" style="left:645px;top:3436px" width="36" height="26" viewBox="0 0 36 26"><path d="M2 24V12q0-9 10-10v5q-5 1-5 5h5v12zM20 24V12q0-9 10-10v5q-5 1-5 5h5v12z" fill="#ddd"/></svg>
<div class="abs" style="left:645px;top:3430px;width:445px;font-size:12.5px;line-height:25px;color:#4a3a30;text-indent:52px">Summit Builders is one of the best general contractors we've worked with. The entire team tactfully delivered a project of exceptional quality while staying on schedule and under budget. We hope to work with Summit Builders again in the near future!"</div>
<svg class="abs" style="left:645px;top:3552px" width="445" height="40" viewBox="0 0 445 40"><path d="M0 1h55l30 30V1h360" fill="none" stroke="#ddd"/></svg>
<div class="abs" style="left:727px;top:3566px;font-family:'Raleway',sans-serif;font-weight:800;font-size:15px;color:var(--orange)">ELENA PORTER</div>
<div class="abs" style="left:727px;top:3585px;font-size:13px;color:#4a3a30">Project Manager</div>
<div class="btn" style="left:645px;top:3641px;width:202px;height:36px">View All Client Testimonials</div>

<!-- footer -->
<footer class="abs footer">
  <h4 style="left:45px">QUICK INFO</h4><div class="uline" style="left:45px"></div>
  <div class="txt" style="left:45px;top:131px;line-height:29.3px">Home<br>About Us<br>Services<br>Projects / Portfolio<br>Contact Us</div>

  <h4 style="left:237px">CONTACT US</h4>
  <div class="txt" style="left:237px;top:131px"><span class="lbl">Address</span><br>412 Cedar Grove Ave<br>Riverton, CA 90000</div>
  <div class="txt" style="left:237px;top:200px"><span class="lbl">Daniel R Hollis</span><br>Branch Manager<br>Office : 555-014-2290<br>Direct : 555-014-7731</div>
  <div class="txt" style="left:237px;top:287px;font-size:10.5px"><span class="lbl">E-mail</span><br>office@summitbuildersca.example</div>

  <h4 style="left:482px">WORKING HOURS</h4>
  <div class="txt" style="left:482px;top:131px;width:270px">we work 7 days a week, every day excluding major holidays. contact us if you have an emergency, with our hotline and contact form.</div>
  <div class="txt" style="left:482px;top:214px;line-height:24px">Monday – Friday<br>Saturday:<br>Sunday And Holidays:</div>
  <div class="txt" style="left:675px;top:214px;line-height:24px">10:00 – 16:00<br>12:00 – 15:00<br>09:00 – 12:00</div>

  <h4 style="left:839px;top:73px">LET'S DISCUSS WHAT'S NEXT</h4>
  <div class="txt" style="left:839px;top:100px">Have a project or a Question? We'd Love to hear from you.</div>
</footer>
<div class="field" style="top:3896px"><svg width="12" height="12" viewBox="0 0 12 12"><circle cx="6" cy="3.5" r="3" fill="#e0cfc2"/><path d="M0 12q6-8 12 0z" fill="#e0cfc2"/></svg>Name</div>
<div class="field" style="top:3945px"><svg width="12" height="10" viewBox="0 0 12 10"><rect width="12" height="10" fill="#e0cfc2"/><path d="M0 0l6 5 6-5" stroke="#4a3324" fill="none"/></svg>Email</div>
<div class="field" style="top:3992px"><svg width="12" height="12" viewBox="0 0 16 16"><path d="M3 1l3 3-2 2c1 2 3 4 5 5l2-2 3 3-2 3C7 15 1 9 1 3z" fill="#e0cfc2"/></svg>Phone</div>
<div class="field" style="top:4040px;height:58px;align-items:flex-start;padding-top:9px"><svg width="13" height="11" viewBox="0 0 13 11"><path d="M1 1h11v7H5l-3 3V8H1z" fill="none" stroke="#e0cfc2" stroke-width="1.3"/></svg>Message</div>
<div class="btn" style="left:839px;top:4118px;width:116px;height:31px">Submit Now</div>

<div class="abs copy">Copyright © 2020 Summit Builders &nbsp;|&nbsp; All Right Reserved</div>

</body>
</html>
```